Postcard double sided

Title: DWIGHT'S REVENGE

Why would Dwight Kessler align himself with Gordon Pruett?

(photo of two guys)

Dwight approached elected officials that he wanted to run for office, but did not have money to finance his campaign. He wanted other elected officials to finance his campaign. Everyone told him that they would help him get the vote out, but that he needed to finance his own race.

In comes Gordon Pruett.

Gordon Pruett who has a pay to play scheme over at the City, told Dwight he would finance his campaign on one condition.

He needed to run against Steven Hulse.

Why would Dwight want to run with no money?

Backside

DWIGHT'S REVENGE

Dwight decided to run because no one on the school board would terminate Dwight's ex and her new boyfriend who both work for the school district. His ex even filed criminal charges against him that are still pending.

Mug Shot facing left (name the charges Criminal Trespass , and Criminal Mischief (highlight bold letters use two lines) mug shot facing right

Complaint one (then photo with full face) Compliant 2)
(showcharges)

Dwight's ultimate goal is to terminate his ex and her new boyfriend if elected.
Plus Gordon Pruett needs the majority on the school board to do what he does bet.

Kickbacks for Contracts.

They will hire their own contractors!
Say "No" to Dwight's Revenge and Gordon Pruett Money Grab!

Title On Back: all caps: DOMESTIC VIOLENCE

```html
<!DOCTYPE html>
<html lang="en">
<head>
<meta charset="utf-8">
<title>Dwight's Revenge – Postcard</title>
<link href="https://fonts.googleapis.com/css2?family=Anton&family=Archivo:wght@800&family=Comic+Neue:wght@400;700&family=Oswald:wght@700&family=Arimo:wght@400;700&display=swap" rel="stylesheet">
<style>
  :root{
    --navy:#0d5fa6;
    --blue:#1a8ad3;
    --sky:#5cc3ee;
    --back-blue:#1674b6;
    --title-dark:#1565a8;
    --title-light:#2b90d6;
    --ink:#2a2a2a;
    --white:#ffffff;
    --label-pink:#e23a93;
    --frame:#9a9a9a;
  }
  *{margin:0;padding:0;box-sizing:border-box}
  html,body{width:894px;height:1200px;overflow:hidden;background:var(--white)}
  .sheet{position:relative;width:894px;height:1200px}

  .card{position:absolute;left:58px;width:778px;height:518px;overflow:hidden}
  .card--front{top:26px;background:var(--white);outline:1px solid var(--frame)}
  .card--back{top:610px;background:var(--back-blue)}

  .side-label{position:absolute;font-family:Arimo,Arial,sans-serif;font-weight:400;font-size:29px;color:var(--label-pink)}
  .side-label--front{left:652px;top:556px}
  .side-label--back{left:671px;top:1148px}

  /* front */
  .front-shape{position:absolute;left:0;top:0}
  .duo-photo{position:absolute;left:3px;top:77px;width:385px;height:441px;
    background:linear-gradient(180deg,#3a4452 0%,#23272f 55%,#4a3a34 100%)}
  .headline{position:absolute;left:0;top:297px}
  .headline__line{display:block;height:44px;padding-left:51px;
    font-family:Oswald,"Arial Narrow",sans-serif;font-weight:700;font-size:36px;line-height:44px;color:var(--white);white-space:nowrap}
  .headline__line--dark{background:var(--navy)}
  .headline__line--light{background:var(--blue)}
  .headline__line:nth-child(1){width:294px}
  .headline__line:nth-child(2){width:390px}
  .headline__line:nth-child(3){width:294px}
  .headline__line:nth-child(4){width:356px}

  .title{position:absolute;left:478px;top:34px;width:222px;text-align:center;font-family:Archivo,Arial,sans-serif;font-weight:800;line-height:1}
  .title__name{display:block;font-size:44px;color:var(--title-dark);letter-spacing:.5px}
  .title__word{display:block;font-size:38px;color:var(--title-light);margin-top:-2px}

  .story{position:absolute;left:432px;top:121px;width:336px;font-family:"Comic Neue","Comic Sans MS",cursive;font-size:15px;line-height:20.8px;color:var(--ink)}
  .story p{margin-bottom:20.8px}
  .story p.tight{margin-bottom:0}

  /* back */
  .mug-photo{position:absolute;left:500px;top:10px;width:278px;height:508px;
    background:radial-gradient(ellipse at 55% 40%,#5aa9dc 0%,#2b82c2 45%,var(--back-blue) 80%)}
  .back-title{position:absolute;left:48px;top:40px;font-family:Anton,Impact,sans-serif;font-size:50px;line-height:1.1;color:var(--white);letter-spacing:4px}
  .back-copy{position:absolute;left:48px;top:104px;width:440px;font-family:"Comic Neue","Comic Sans MS",cursive;font-size:14.4px;line-height:20.5px;color:var(--white)}
  .back-copy p{margin-bottom:20.5px}
  .back-copy p:last-child{margin-bottom:0}
  .complaint{position:absolute;top:362px;width:112px;height:150px;background:var(--white)}
  .complaint--one{left:28px}
  .complaint--two{left:153px}
  .callout{position:absolute;left:298px;top:360px;width:180px;color:var(--white)}
  .callout__lead{font-family:"Comic Neue","Comic Sans MS",cursive;font-size:14.4px;line-height:20px}
  .callout__cta{margin-top:2px;font-family:Arimo,Arial,sans-serif;font-weight:700;font-size:18px;line-height:22px}
  .rule{position:absolute;left:523px;width:230px;height:1px;background:rgba(255,255,255,.75)}
  .rule--1{top:355px}.rule--2{top:392px}.rule--3{top:429px}.rule--4{top:467px}
</style>
</head>
<body>
<div class="sheet">

  <section class="card card--front">
    <svg class="front-shape" width="778" height="518" viewBox="0 0 778 518">
      <path d="M0 0 H426 C400 150 385 330 398 410 C408 470 440 500 474 518 H0 Z" fill="var(--sky)"/>
      <path d="M0 0 H408 C384 150 370 330 382 410 C392 470 418 500 450 518 H0 Z" fill="var(--blue)"/>
      <path d="M0 0 H394 C370 150 356 330 368 410 C378 470 402 500 432 518 H0 Z" fill="var(--navy)"/>
    </svg>
    <div class="duo-photo" role="img" aria-label="Photo of two men in suits smiling side by side"></div>
    <h1 class="headline">
      <span class="headline__line headline__line--dark">Why would</span>
      <span class="headline__line headline__line--light">Dwight Kessler align</span>
      <span class="headline__line headline__line--dark">himself with</span>
      <span class="headline__line headline__line--light">Gordon Pruett?</span>
    </h1>
    <h2 class="title">
      <span class="title__name">DWIGHT'S</span>
      <span class="title__word">REVENGE</span>
    </h2>
    <div class="story">
      <p>Dwight approached elected officials that he wanted to run for office, but did not have money to finance his campaign. He wanted other elected officials to finance his campaign. Everyone told him that they would help him get the vote out, but that he needed to finance his own race.</p>
      <p class="tight">In comes Gordon Pruett.</p>
      <p>Gordon Pruett who has a pay to play scheme over at the City, told Dwight he would finance his campaign on one condition.</p>
      <p>He needed to run against Steven Hulse.</p>
      <p>Why would Dwight want to run with no money?</p>
    </div>
  </section>
  <div class="side-label side-label--front">FRONT</div>

  <section class="card card--back">
    <div class="mug-photo" role="img" aria-label="Blue-tinted portrait photo of a man"></div>
    <h2 class="back-title">DOMESTIC VIOLENCE</h2>
    <div class="back-copy">
      <p>Dwight decided to run because no one on the school board would terminate Dwight's ex and her new boyfriend who both work for the school district. His ex even filed criminal charges against him that are still pending.</p>
      <p>Mug Shot facing left (name the charges Criminal Trespass , and Criminal Mischief (highlight bold letters use two lines) mug shot facing right</p>
      <p>Dwight's ultimate goal is to terminate his ex and her new boyfriend if elected. Plus Gordon Pruett needs the majority on the school board to do what he does bet.Kickbacks for Contracts.</p>
    </div>
    <div class="complaint complaint--one" role="img" aria-label="Scan of criminal complaint document one"></div>
    <div class="complaint complaint--two" role="img" aria-label="Scan of criminal complaint document two"></div>
    <div class="callout">
      <p class="callout__lead">They will hire their own contractors!</p>
      <p class="callout__cta">Say "No" to Dwight's Revenge &amp; Gordon Pruett Money Grab!</p>
    </div>
    <div class="rule rule--1"></div>
    <div class="rule rule--2"></div>
    <div class="rule rule--3"></div>
    <div class="rule rule--4"></div>
  </section>
  <div class="side-label side-label--back">BACK</div>

</div>
</body>
</html>
```